Investment Management Firm Power point template

Kestrel Holdings is a real estate investment firm focused on buying commercial office and residential property in the UK. We produce powerpoint presentations for our Board of Directors, Investment Committee and also to external investors.

We are looking for a powerpoint design template which we can use for future presentations which provide a professional look and feel.

Our current website: http://www.kestrelholdings-example.co.uk/

Target Market(s)

Institution Investors, Board of Directors, Professionals

Industry/Entity Type

Real Estate

Requirements
Must have
• Leverage off the current logo and colour scheme. However, does not have to purely rely on this colour scheme.
• - Title page
• - Content Page
• - Slide where graphs can be incorporated
• - Slide where photos can be incorporated
• - Slide of UK Map which can show where the property portfolio is currently located
• - Other slides incorporating smart art or other designs that can be used for future presentations
Nice to have
• An example of graphics that we would love to have in the powerpoint pack which we can easily edit has been attached

```html
<!DOCTYPE html>
<html lang="en">
<head>
<meta charset="utf-8">
<title>Kestrel Holdings – Presentation Template</title>
<link rel="stylesheet" href="https://fonts.googleapis.com/css2?family=Arimo:wght@400;700&display=swap">
<style>
  :root{
    --navy:#35586f;
    --navy-dark:#294559;
    --navy-panel:#3f6179;
    --title-blue:#3a6482;
    --grey-box:#d9d9d9;
    --frame:#cfcfcf;
    --red:#c8202a;
    --sky:#4aa8d8;
    --bar:#345a78;
    --crane-area:#eef0f2;
    --white:#ffffff;
    --gold:#f2d21b;
    --orange:#e8632a;
    --green:#2faa4a;
    --crimson:#d9252f;
  }
  *{margin:0;padding:0;box-sizing:border-box}
  html,body{width:691px;height:1200px;overflow:hidden;background:var(--white)}
  body{position:relative;font-family:"Arimo",Arial,sans-serif}
  .slide{position:absolute;left:33px;width:623px;overflow:hidden}
  .slide--title{top:25px;height:372px;background:var(--navy)}
  .slide--agenda{top:408px;height:373px;border:1px solid var(--frame);background:var(--white)}
  .slide--historical{top:797px;height:372px;border:1px solid var(--frame);background:var(--white)}
  .photo{position:absolute}
  .skyline{background:linear-gradient(180deg,#7c8a98 0%,#d8a560 55%,#3b3830 80%,#1f2328 100%)}
  .title-strip{position:absolute;left:0;top:128px;width:623px;height:90px;background:var(--navy-dark)}
  .title-photo{left:0;top:132px;width:174px;height:84px}
  .title-panel{position:absolute;left:174px;top:114px;width:449px;height:136px;background:var(--navy-panel);display:flex;align-items:center;padding-left:24px}
  .wordmark{color:var(--white);font-weight:700;white-space:nowrap}
  .title-panel .wordmark{font-size:44px;letter-spacing:-.5px}
  .header-band{position:absolute;left:0;top:0;width:623px;height:58px;background:var(--navy)}
  .header-photo{left:0;top:0;width:122px;height:55px}
  .header-logo{position:absolute;right:0;top:0;width:218px;height:58px;display:flex;align-items:center;justify-content:center;background:var(--navy-dark)}
  .header-logo .wordmark{font-size:21px}
  .section-title{position:absolute;right:0;top:60px;height:45px;background:var(--grey-box);color:var(--title-blue);font-weight:700;display:flex;align-items:center;justify-content:center;letter-spacing:.5px}
  .slide--agenda .section-title{width:216px;font-size:32px}
  .slide--historical .section-title{width:218px;font-size:27px}
  .shape-art{position:absolute;left:0;top:0}
  .chart{position:absolute;left:0;top:0}
  .chart text{font-family:"Arimo",Arial,sans-serif}
</style>
</head>
<body>

<section class="slide slide--title">
  <div class="title-strip"></div>
  <div class="photo skyline title-photo" role="img" aria-label="City skyline at sunset with a tall glass tower beside the river"></div>
  <div class="title-panel"><span class="wordmark">Kestrel Holdings</span></div>
</section>

<section class="slide slide--agenda">
  <div class="header-band"></div>
  <div class="photo skyline header-photo" role="img" aria-label="City skyline at sunset"></div>
  <div class="header-logo"><span class="wordmark">Kestrel Holdings</span></div>
  <div class="section-title">AGENDA</div>
  <svg class="shape-art" width="623" height="373" viewBox="0 0 623 373">
    <defs>
      <linearGradient id="boardroom" x1="0" y1="0" x2="1" y2="1">
        <stop offset="0" stop-color="#4a4440"/>
        <stop offset=".5" stop-color="#2a2523"/>
        <stop offset="1" stop-color="#12100f"/>
      </linearGradient>
      <filter id="iconShadow" x="-30%" y="-30%" width="160%" height="160%">
        <feDropShadow dx="1" dy="2" stdDeviation="2" flood-opacity=".45"/>
      </filter>
    </defs>
    <path role="img" aria-label="Modern boardroom with a long conference table and leather chairs" d="M0 55 H235 Q228 200 170 373 H0 Z" fill="url(#boardroom)"/>
    <g filter="url(#iconShadow)" fill="#fff">
      <circle cx="229" cy="100" r="20"/><circle cx="220" cy="148" r="20"/>
      <circle cx="214" cy="194" r="20"/><circle cx="207" cy="244" r="20"/>
      <circle cx="193" cy="291" r="20"/><circle cx="185" cy="340" r="20"/>
    </g>
    <g fill="var(--navy-dark)" stroke="var(--navy-dark)" stroke-width="1.5">
      <rect x="221" y="90" width="15" height="20" fill="none"/>
      <line x1="224" y1="96" x2="233" y2="96"/><line x1="224" y1="100" x2="233" y2="100"/><line x1="224" y1="104" x2="233" y2="104"/>
      <rect x="210" y="138" width="20" height="13" fill="none"/>
      <line x1="220" y1="151" x2="220" y2="158"/><line x1="215" y1="158" x2="225" y2="158"/>
      <circle cx="214" cy="190" r="4" stroke="none"/><path d="M206 203 Q214 193 222 203 Z" stroke="none"/>
      <circle cx="207" cy="237" r="3.5" stroke="none"/><circle cx="200" cy="249" r="3" stroke="none"/><circle cx="214" cy="249" r="3" stroke="none"/>
      <line x1="207" y1="241" x2="200" y2="246"/><line x1="207" y1="241" x2="214" y2="246"/>
      <circle cx="193" cy="291" r="9" fill="none"/><line x1="184" y1="291" x2="202" y2="291"/><ellipse cx="193" cy="291" rx="4" ry="9" fill="none"/>
      <line x1="185" y1="349" x2="185" y2="330"/><path d="M180 335 L185 329 L190 335 Z" stroke="none"/>
      <line x1="185" y1="342" x2="176" y2="346"/><line x1="185" y1="342" x2="194" y2="346"/>
    </g>
  </svg>
</section>

<section class="slide slide--historical">
  <div class="header-band"></div>
  <div class="photo skyline header-photo" role="img" aria-label="City skyline at sunset"></div>
  <div class="header-logo"><span class="wordmark">Kestrel Holdings</span></div>
  <div class="section-title">HISTORICAL</div>
  <svg class="chart" width="623" height="372" viewBox="0 0 623 372">
    <defs>
      <linearGradient id="nightCity" x1="0" y1="0" x2="0" y2="1">
        <stop offset="0" stop-color="#3d4a5e"/>
        <stop offset=".45" stop-color="#6c5a48"/>
        <stop offset=".75" stop-color="#2f5b7a"/>
        <stop offset="1" stop-color="#1d3850"/>
      </linearGradient>
    </defs>
    <polygon role="img" aria-label="Aerial view of the city at dusk with the river and a lit bridge" points="0,58 235,58 178,372 0,372" fill="url(#nightCity)"/>

    <text x="319" y="120" font-size="9" font-weight="700" fill="var(--red)">Market Snapshot</text>

    <rect role="img" aria-label="Tower crane illustration carrying the bar chart" x="283" y="126" width="272" height="150" rx="3" fill="var(--crane-area)"/>

    <line x1="366" y1="144" x2="550" y2="144" stroke="var(--sky)" stroke-width="1.2"/>
    <path d="M550 141 L556 144 L550 147 Z" fill="var(--sky)"/>
    <text x="374" y="141" font-size="7" fill="#333">2%</text>
    <text x="445" y="141" font-size="6" fill="#333" text-anchor="middle">% of Stock</text>
    <text x="527" y="141" font-size="7" fill="#333">5%</text>

    <text x="300" y="181" font-size="6" fill="#333">0</text>
    <text x="294" y="215" font-size="4" fill="#333">m sq ft</text>
    <text x="300" y="253" font-size="6" fill="#333">3</text>
    <line x1="308" y1="179" x2="330" y2="179" stroke="#999" stroke-width=".5"/>
    <line x1="308" y1="251" x2="330" y2="251" stroke="#999" stroke-width=".5"/>

    <line x1="365" y1="178" x2="548" y2="178" stroke="#555" stroke-width="1"/>

    <g fill="var(--bar)">
      <rect x="370" y="178" width="13" height="14"/>
      <rect x="388" y="178" width="13" height="12"/>
      <rect x="406" y="178" width="13" height="23"/>
      <rect x="424" y="178" width="13" height="8"/>
      <rect x="442" y="178" width="13" height="6"/>
      <rect x="460" y="178" width="13" height="8"/>
      <rect x="478" y="178" width="13" height="60"/>
      <rect x="496" y="178" width="13" height="72"/>
      <rect x="514" y="178" width="13" height="12"/>
      <rect x="532" y="178" width="13" height="6"/>
    </g>
    <g font-size="5.5" fill="var(--bar)" text-anchor="middle">
      <text x="376.5" y="199">0.5m</text>
      <text x="394.5" y="197">0.4m</text>
      <text x="412.5" y="208">0.9m</text>
      <text x="430.5" y="193">0.3m</text>
      <text x="448.5" y="191">0.2m</text>
      <text x="466.5" y="193">0.3m</text>
      <text x="484.5" y="245">2.3m</text>
      <text x="502.5" y="257">2.8m</text>
      <text x="520.5" y="197">0.4m</text>
      <text x="538.5" y="191">0.2m</text>
    </g>
    <g font-size="4.5" fill="#333">
      <text transform="translate(375 202) rotate(90)">Edinburgh</text>
      <text transform="translate(393 200) rotate(90)">Glasgow</text>
      <text transform="translate(411 211) rotate(90)">Manchester</text>
      <text transform="translate(429 196) rotate(90)">Midlands</text>
      <text transform="translate(447 194) rotate(90)">Oxbridge</text>
      <text transform="translate(465 196) rotate(90)">Cambridge</text>
      <text transform="translate(483 248) rotate(90)">City</text>
      <text transform="translate(501 260) rotate(90)">West End</text>
      <text transform="translate(519 200) rotate(90)">Reading</text>
      <text transform="translate(537 194) rotate(90)">Slough</text>
    </g>

    <text x="445" y="288" font-size="8" font-weight="700" fill="var(--red)" text-anchor="middle">2014 Total Returns</text>
    <g fill="var(--bar)">
      <circle cx="331" cy="330" r="27"/><circle cx="399" cy="330" r="27"/>
      <circle cx="464" cy="330" r="27"/><circle cx="528" cy="330" r="27"/>
    </g>
    <g font-size="30" font-weight="700" text-anchor="middle">
      <text x="331" y="343" fill="var(--gold)">£</text>
      <text x="399" y="343" fill="var(--orange)">£</text>
      <text x="464" y="343" fill="var(--green)">£</text>
      <text x="528" y="343" fill="var(--crimson)">£</text>
    </g>
    <g font-size="4.5" font-weight="700" fill="var(--white)" text-anchor="middle">
      <text x="331" y="313">Rest of UK</text><text x="399" y="313">City</text>
      <text x="464" y="313">South East</text><text x="528" y="310">West End</text><text x="528" y="315">Midtown</text>
      <text x="331" y="351">15.9%</text><text x="399" y="351">23.3%</text>
      <text x="464" y="351">22.9%</text><text x="528" y="351">24.0%</text>
    </g>
  </svg>
</section>

</body>
</html>
```